Redesign of Form/Document Navigation Page

I need a redesign of our document and navigation bar on the left. We want the same navigation bar layout/setup but want the buttons and typography to be simple and matching all over. The form needs to be aesthetically pleasing and fit within the page.

1st attachment is our Direct Deposit and the second is the form continued.

```html
<!DOCTYPE html>
<html lang="en">
<head>
<meta charset="utf-8">
<title>Sentinel Watch Services – Direct Deposit</title>
<link href="https://fonts.googleapis.com/css2?family=Open+Sans:wght@400;600;700&display=swap" rel="stylesheet">
<style>
  :root {
    --page-bg: #f2f2f2;
    --white: #ffffff;
    --ink: #3a3a3a;
    --muted: #6d6d6d;
    --brand-gold: #e9ad1f;
    --brand-gold-dark: #d99d12;
    --nav-blue-top: #3c73b6;
    --nav-blue-bottom: #24518f;
    --field-bg: #eef1f4;
    --field-line: #dde2e7;
    --rule: #d6d6d6;
    --social: #2d5a98;
  }
  * { box-sizing: border-box; margin: 0; padding: 0; }
  html, body { width: 1200px; height: 907px; overflow: hidden; }
  body {
    position: relative;
    background: var(--page-bg);
    font-family: "Open Sans", Arial, sans-serif;
    color: var(--ink);
  }
  .site-header {
    position: absolute; left: 0; top: 0; width: 1200px; height: 91px;
    background: var(--white); border-bottom: 2px solid var(--rule);
  }
  .brand {
    position: absolute; left: 130px; top: 26px;
    display: flex; align-items: center; gap: 9px;
  }
  .brand-mark { width: 30px; height: 30px; border-radius: 50%; background: var(--nav-blue-bottom); }
  .brand-name {
    font-weight: 700; font-size: 19px; line-height: 19px; color: var(--brand-gold);
    text-transform: uppercase; width: 200px;
  }
  .top-nav { position: absolute; top: 42px; display: flex; align-items: center; gap: 7px; font-size: 14px; color: #333; }
  .top-nav svg { fill: #9a9a9a; }
  .top-nav.home { left: 738px; }
  .top-nav.help { left: 842px; }
  .user-chip {
    position: absolute; left: 961px; top: 35px; width: 113px; height: 33px;
    background: #e3e3e3; border: 1px solid #d4d4d4;
    display: flex; align-items: center; justify-content: center; gap: 7px;
    font-size: 13.5px; color: #444;
  }
  .user-chip svg { fill: #7d7d7d; }

  .side-nav { position: absolute; left: 137px; top: 138px; }
  .side-link {
    position: relative; width: 230px; height: 42px; margin-bottom: 9px;
    background: linear-gradient(var(--nav-blue-top), var(--nav-blue-bottom));
    color: var(--white); font-size: 15.5px; letter-spacing: .2px;
    display: flex; align-items: center; padding-left: 56px; margin-left: 0;
  }
  .side-icon {
    position: absolute; left: 0; top: 50%; transform: translateY(-50%);
    width: 47px; height: 47px; border-radius: 50%;
    background: var(--nav-blue-bottom); border: 3px solid var(--brand-gold);
    display: flex; align-items: center; justify-content: center;
  }
  .side-icon svg { width: 22px; height: 22px; fill: none; stroke: var(--white); stroke-width: 2; }

  .document-panel {
    position: absolute; left: 379px; top: 137px; width: 685px; height: 667px;
    background: var(--white); border: 1px solid #cfcfcf;
  }
  .notice-title { position: absolute; left: 28px; top: 29px; font-size: 14.8px; color: #333; }
  .notice-body { position: absolute; left: 27px; top: 63px; width: 615px; font-size: 12.2px; line-height: 20px; color: var(--muted); }
  .notice-body p + p { margin-top: 6px; }
  .field-label { position: absolute; font-size: 13.8px; color: #666; }
  .field {
    position: absolute; background: var(--field-bg); border: 1px solid var(--field-line);
  }
  .btn {
    position: absolute; background: var(--brand-gold); color: var(--white);
    font-weight: 700; font-size: 14.5px; display: flex; align-items: center; justify-content: center;
    border-bottom: 2px solid var(--brand-gold-dark);
  }

  .manager-sign {
    position: absolute; left: -1px; top: 436px; width: 685px; height: 231px;
    background: linear-gradient(#427dbd, #1f4f90);
  }
  .manager-title {
    position: absolute; left: 0; top: 25px; width: 100%;
    display: flex; align-items: center; justify-content: center; gap: 7px;
    color: var(--white); font-size: 17.5px; font-weight: 600;
  }
  .manager-title::before, .manager-title::after { content: ""; width: 40px; height: 1px; background: rgba(255,255,255,.6); }
  .input-box {
    position: absolute; background: var(--white); border: 1px solid #c9d3df;
    font-size: 12.5px; color: #8a8a8a; padding: 10px 13px;
  }

  .site-footer {
    position: absolute; left: 0; top: 832px; width: 1200px; height: 75px;
    background: var(--white); border-top: 2px solid var(--rule);
  }
  .copyright { position: absolute; left: 133px; top: 33px; font-size: 13px; color: #444; }
  .social { position: absolute; left: 928px; top: 25px; display: flex; gap: 3px; }
  .social span { width: 32px; height: 32px; border-radius: 50%; border: 2px solid var(--social); }
</style>
</head>
<body>
  <header class="site-header">
    <div class="brand"><span class="brand-mark"></span><span class="brand-name">Sentinel Watch Services</span></div>
    <div class="top-nav home">
      <svg width="20" height="18" viewBox="0 0 20 18"><path d="M10 1 1 9h3v8h4v-5h4v5h4V9h3z"/></svg>HOME
    </div>
    <div class="top-nav help">
      <svg width="22" height="18" viewBox="0 0 22 18"><ellipse cx="11" cy="8" rx="10" ry="7"/><path d="M5 13 3 18l6-4z"/></svg>HELP
    </div>
    <div class="user-chip">
      <svg width="14" height="15" viewBox="0 0 14 15"><circle cx="7" cy="4" r="3.5"/><path d="M0 15c0-5 3-7 7-7s7 2 7 7z"/></svg>Dana Reyes
    </div>
  </header>

  <nav class="side-nav">
    <a class="side-link"><span class="side-icon"><svg viewBox="0 0 24 24"><rect x="2" y="6" width="20" height="12" rx="1"/><circle cx="12" cy="12" r="3"/></svg></span>Direct Deposit</a>
    <a class="side-link"><span class="side-icon"><svg viewBox="0 0 24 24" style="fill:#fff;stroke:none"><path d="M4 9h4a3 3 0 1 1 5 0h4v4a3 3 0 1 1 0 5v3H4z"/></svg></span>Change W-4</a>
    <a class="side-link"><span class="side-icon"><svg viewBox="0 0 24 24"><circle cx="12" cy="12" r="4"/><path d="M12 2v4M12 18v4M2 12h4M18 12h4M5 5l3 3M16 16l3 3M5 19l3-3M16 8l3-3"/></svg></span>Labour Code</a>
    <a class="side-link"><span class="side-icon"><svg viewBox="0 0 24 24"><circle cx="12" cy="12" r="10"/><path d="M12 10v7M12 6v1"/></svg></span>Personal Information</a>
    <a class="side-link"><span class="side-icon"><svg viewBox="0 0 24 24"><path d="M3 10v4h4l9 5V5L7 10zM7 14l2 6"/></svg></span>Appraisal and Review</a>
    <a class="side-link"><span class="side-icon"><svg viewBox="0 0 24 24"><rect x="3" y="8" width="11" height="13"/><path d="M9 8V3h12v13h-7"/></svg></span>Write Up-Slip</a>
    <a class="side-link"><span class="side-icon"><svg viewBox="0 0 24 24"><path d="M3 3v18h18M6 16l5-5 3 3 6-7"/></svg></span>Employee Performance</a>
  </nav>

  <main class="document-panel">
    <h1 class="notice-title" style="font-weight:400">IMPORTANT! please read and sign before completing and submitting</h1>
    <div class="notice-body">
      <p>Captain &amp; Maritime eleifend libero a tempus libero lectus feugiat felis Morbi diam mauris viverra in gravida eu mattis in ante Morbi eget arcu Morbi porta libero id ullamcorper nonummy nibh ligula pulvinar metus eget consectetuer augue nisi quis lacus Ut ac mi quis lacus mollis aliquam Curabitur</p>
      <p>commodo a mi Morbi ornare gravida elit Integer congue augue et malesuada iaculis ipsum dui aliquet felis at cursus magna nisl nec elit Praesent elementum elit at te</p>
    </div>
    <span class="field-label" style="left:21px;top:193px">Employee Name:</span>
    <span class="field-label" style="left:21px;top:218px">Employee Signature</span>
    <span class="field-label" style="left:254px;top:218px">Sign Date:</span>
    <div class="field" style="left:23px;top:242px;width:225px;height:32px"></div>
    <div class="field" style="left:255px;top:242px;width:225px;height:32px"></div>
    <div class="field" style="left:23px;top:283px;width:225px;height:70px"></div>
    <div class="btn" style="left:23px;top:367px;width:225px;height:39px">Accept Document</div>

    <section class="manager-sign">
      <h2 class="manager-title">ONLINE PAYROLL MANAGER SIGNS BELOW</h2>
      <div class="input-box" style="left:32px;top:69px;width:257px;height:36px">Company Name</div>
      <div class="input-box" style="left:34px;top:117px;width:258px;height:36px">Employee File Number</div>
      <div class="input-box" style="left:299px;top:69px;width:352px;height:84px">Comments</div>
      <div class="btn" style="left:35px;top:164px;width:172px;height:37px">Sign Up Now</div>
    </section>
  </main>

  <footer class="site-footer">
    <p class="copyright">© 2016 Company Name &nbsp;All right reserved &nbsp;Term of Use</p>
    <div class="social" aria-label="Social links"><span></span><span></span><span></span><span></span></div>
  </footer>
</body>
</html>
```